Flyer for The Quiet Bloom Gathering

I am launching my new offering in my business at an event next Sunday where I have a booth and need a flyer advertising the offering, so the flyer needs to stand out for other practitioners that will also be there on the day offering there services.
This flyer is also what I will use for marketing on social media as well as on the day of the event. See the link below to the offering
http://sarahlindqvist.com.au/quiet-bloom-gathering/

Target Market(s)

Women with body image issues - age range 25 - 65
Women with issues around food such as binge eating, emotional eating, eating disorders.

Industry/Entity Type

Health And Wellness

Font styles to use
Serif
Sans Serif
Script

Colors
f9d9e8
85cae6
cee9f5
fee18a
ffffff
eea4c8

Requirements
Must have
• Colours matching my overall website at sarahlindqvist.com.au - pinks, light blue, gold, white
• Imagery similiar to my Instagram, see below https://www.instagram.com/riverstonecarexy/
• - soft, warm, welcoming, nurturing, safe, inviting - see image on sales page for inspiration
• contact details
Should not have
• harsh dark colours or harsh lines

```html
<!DOCTYPE html>
<html lang="en">
<head>
<meta charset="utf-8">
<title>The Quiet Bloom Gathering – Flyer</title>
<link rel="stylesheet" href="https://fonts.googleapis.com/css2?family=Montserrat:wght@300;400;500;600&family=Cabin+Condensed:wght@500&family=Cabin:ital,wght@1,500&family=Lato:wght@400;700&display=swap">
<style>
  :root{
    --canvas:#e7eef0;
    --paper:#ffffff;
    --ink:#2b2b2b;
    --night:#222325;
    --pink:#ec4f9d;
    --pink-soft:#ef7fb6;
    --blue:#5bb7dd;
    --blue-bar:#85cae6;
    --blue-pale:#cee9f5;
    --gold-pale:#fde9b6;
    --tag:#1f6fb3;
  }
  *{margin:0;padding:0;box-sizing:border-box}
  html,body{width:1200px;height:1200px;overflow:hidden;background:var(--canvas)}
  body{font-family:"Montserrat",sans-serif;color:var(--ink)}
  .flyer{position:absolute;left:187px;top:20px;width:826px;height:1160px;background:var(--paper);overflow:hidden}
  .header{position:absolute;left:0;top:0;width:826px;height:345px}
  .header-art{position:absolute;left:0;top:0}
  .brand{position:absolute;left:0;width:380px;text-align:center;color:#fff}
  .brand-name{top:62px;font-size:27px;font-weight:400;color:var(--pink-soft);letter-spacing:.5px}
  .title-top{top:123px;font-size:28px;font-weight:300}
  .title-main{top:158px;font-size:33px;font-weight:600;color:var(--blue);letter-spacing:.3px}
  .connect{top:204px;font-size:15px;font-weight:500;color:var(--pink)}
  .phone-icon{position:absolute;left:173px;top:232px;width:34px;height:34px}
  .phone-num{top:272px;font-family:"Lato",sans-serif;font-size:23px}
  .intro{position:absolute;left:0;top:363px;width:826px;text-align:center;font-size:15px;line-height:19.3px}
  .pink{color:var(--pink)}
  .accent{font-family:"Cabin",sans-serif;font-style:italic;font-weight:500;color:var(--pink);font-size:14.5px}
  .accent-up{font-family:"Cabin Condensed",sans-serif;font-weight:500;color:var(--pink);font-size:15px}
  .band{position:absolute;left:0;top:571px;width:818px;height:77px;background:var(--gold-pale);text-align:center;font-size:13px;line-height:16.5px;padding-top:16px}
  .band .accent-up{font-size:13px}
  .col-left{position:absolute;left:42px;top:672px;width:325px;font-size:12.5px;line-height:16px}
  .col-left p{margin-bottom:6px}
  .col-left .accent{font-size:12px}
  .justify{text-align:justify}
  .offer{position:absolute;left:405px;top:668px;width:411px;height:172px;background:var(--blue-pale);padding:10px 18px 0 22px;font-size:12.5px;line-height:15.5px}
  .offer ul{list-style:none}
  .offer li{position:relative;margin-top:1px}
  .offer li::before{content:"";position:absolute;left:-14px;top:6px;width:5px;height:5px;border-radius:50%;background:var(--pink)}
  .price{position:absolute;left:0;width:826px;text-align:center;font-size:15px}
  .tag{display:inline-block;margin-left:14px;padding:3px 9px 3px 18px;background:var(--tag);color:#fff;font-weight:600;font-size:17px;vertical-align:middle;clip-path:polygon(10px 0,100% 0,100% 100%,10px 100%,0 50%)}
  .gallery{position:absolute;left:48px;top:965px;width:461px;height:107px;background:#1d1d1d;display:flex;gap:12px;padding:9px 11px}
  .gallery div{flex:1}
  .g1{background:linear-gradient(135deg,#cfcfcf,#7a7a7a)}
  .g2{background:linear-gradient(180deg,#d7a6b3,#c88a9d 60%,#e7c2c4)}
  .g3{background:linear-gradient(180deg,#d9ecef,#7fb3b8 55%,#e6d3c4)}
  .ready{position:absolute;left:540px;top:968px}
  .ready-1{font-size:37px;font-weight:500;color:var(--pink-soft);letter-spacing:1px}
  .ready-2{font-size:53px;font-weight:600;font-style:italic;color:var(--blue);line-height:48px}
  .ready-2 span{color:var(--pink-soft);font-style:normal;margin-left:8px}
  .social{position:absolute;left:78px;top:1110px;display:flex;gap:14px}
  .social span{width:29px;height:29px;border-radius:50%;background:var(--pink-soft)}
  .contact-bar{position:absolute;left:287px;top:1102px;width:539px;height:42px;background:var(--blue-bar);color:#fff;font-size:12.5px;display:flex;align-items:center;gap:22px;padding-left:18px}
  .contact-bar svg{vertical-align:-2px;margin-right:6px}
</style>
</head>
<body>
<main class="flyer">
  <header class="header">
    <svg class="header-art" width="826" height="345" viewBox="0 0 826 345">
      <defs>
        <linearGradient id="sky" x1="0" y1="0" x2="0" y2="1">
          <stop offset="0" stop-color="#3e4b63"/>
          <stop offset=".35" stop-color="#c98b95"/>
          <stop offset=".48" stop-color="#f3c49a"/>
          <stop offset=".62" stop-color="#b79aa8"/>
          <stop offset="1" stop-color="#3a4553"/>
        </linearGradient>
      </defs>
      <rect role="img" aria-label="Photo: wooden jetty stretching across a calm lake at sunset" x="0" y="0" width="826" height="345" fill="url(#sky)"/>
      <polygon points="0,0 340,0 480,172 355,345 0,345" fill="none" stroke="#151515" stroke-width="7"/>
      <polygon points="0,0 315,0 455,172 330,345 0,345" fill="var(--night)"/>
    </svg>
    <div class="brand brand-name">Sarah Lindqvist</div>
    <div class="brand title-top">The Quiet Bloom</div>
    <div class="brand title-main">GATHERING</div>
    <div class="brand connect">Connect with Me</div>
    <svg class="phone-icon" viewBox="0 0 34 34"><circle cx="17" cy="17" r="15.5" fill="none" stroke="#fff" stroke-width="1.4"/><path d="M12 10c1-1 2-1 3 0l1.5 2.5c.4.8 0 1.5-.6 2l-.8.6c.8 1.8 2 3 3.8 3.8l.6-.8c.5-.6 1.2-1 2-.6L24 19c1 1 1 2 0 3-1.5 1.5-3.5 1.5-6-.3-2.4-1.7-4.3-3.6-6-6-1.8-2.5-1.8-4.5 0-5.7z" fill="#fff"/></svg>
    <div class="brand phone-num">0400 555 917</div>
  </header>

  <section class="intro">
    <div>It's time to make a commitment....</div>
    <div class="accent-up">It's time for YOU, to SHOW UP for YOU.....</div>
    <div>It's time to truly let go.......and finally heal, and find the peace that you so long for...</div>
    <div>You deserve to feel the freedom that comes with truly loving and accepting your body.</div>
    <div>You deserve the freedom that comes with experiencing a deeper trusting</div>
    <div>connection with your body, where you feel safe, at home.</div>
    <div>Can you even imagine a whole day that you didn't hate your body,</div>
    <div>you didn't fight with food, and you felt peaceful and at home with your body?</div>
    <div class="accent">Can you love the part of you, that hates your body?</div>
    <div class="accent">You can't heal something you hate.</div>
  </section>

  <section class="band">
    <div><span class="accent-up">It's time to show up for YOU</span>, consistently, every week, and do the work, once and for all.</div>
    <div>No more games, <span class="accent-up">no more half in on YOU</span>....</div>
    <div>You deserve better than a life contained in the mental prison of body hatred.</div>
  </section>

  <section class="col-left">
    <p>Are you truly ready to make the commitment? How would it feel to be able to say, "<span class="accent">I am free to love and accept my body</span>", and "<span class="accent">I am free, connected and at peace to my body</span>"?</p>
    <p class="justify">I am inviting 10 women only into this six-week healing experience, as I personally know, that when we share our stories, it opens our hearts for other people to share their stories. It gives us the</p>
  </section>

  <section class="offer">
    <p>The women that come on this six-week journey will receive;</p>
    <ul>
      <li>One 90mins one on one coaching session with me (which for the women that have attended the Friday circle previously, can be done before this healing circle begins);</li>
      <li>Private Online Group to continue support outside of the circle</li>
      <li>Homework outside of circle to support your healing</li>
      <li>Journal and other small gifts weekly</li>
    </ul>
  </section>

  <section class="pricing">
    <div class="price" style="top:860px">The financial investment in YOU, is <span class="pink">$XX</span> ——— for the six weeks.</div>
    <div class="price" style="top:880px">For the women that have attended the Friday night, Soft Light Sister Circle, you will</div>
    <div class="price" style="top:908px">receive a discount of <span class="tag">$100</span></div>
    <div class="price" style="top:940px">taking the price to <span class="pink">$XX</span></div>
  </section>

  <div class="gallery">
    <div class="g1" role="img" aria-label="Black and white photo of a woman in a calm, reflective pose"></div>
    <div class="g2" role="img" aria-label="Photo of a draped wooden shelter on a pink-toned beach"></div>
    <div class="g3" role="img" aria-label="Photo of a woman standing in gentle ocean waves"></div>
  </div>

  <div class="ready">
    <div class="ready-1">Are you</div>
    <div class="ready-2">READY<span>?</span></div>
  </div>

  <nav class="social" aria-label="Social links"><span></span><span></span><span></span><span></span></nav>

  <footer class="contact-bar">
    <span><svg width="13" height="10" viewBox="0 0 13 10"><rect x=".6" y=".6" width="11.8" height="8.8" fill="none" stroke="#fff" stroke-width="1.2"/><path d="M.6 .6 6.5 5.5 12.4 .6" fill="none" stroke="#fff" stroke-width="1.2"/></svg>sarah@sarahlindqvist.com.au</span>
    <span><svg width="12" height="12" viewBox="0 0 12 12"><circle cx="6" cy="6" r="5.3" fill="none" stroke="#fff" stroke-width="1.2"/><path d="M.7 6h10.6M6 .7c-3 3-3 7.6 0 10.6M6 .7c3 3 3 7.6 0 10.6" fill="none" stroke="#fff" stroke-width="1"/></svg>www.sarahlindqvist.com.au</span>
  </footer>
</main>
</body>
</html>
```